Boutique Technology Consultancy specialising is Electronic and physical security

We need to redo our existing outdated website. For your reference the link www.brivo.com.au

```html
<!DOCTYPE html>
<html lang="en">
<head>
<meta charset="utf-8">
<title>Talvera Services</title>
<link href="https://fonts.googleapis.com/css2?family=Exo+2:wght@300;400&family=Maven+Pro:wght@500;600&family=Montserrat:wght@400;500;600;700&display=swap" rel="stylesheet">
<style>
:root{
  --red:#d7201f;
  --gold:#e2aa4d;
  --navy:#2c2b3d;
  --card:#353447;
  --card-line:#4a495c;
  --team:#231f20;
  --light:#eeeeee;
  --text:#2a2a2a;
  --muted:#555;
  --white:#fff;
  --purple:#7a6fd6;
}
*{box-sizing:border-box;margin:0;padding:0}
html,body{width:1200px;height:3904px;overflow:hidden}
body{font-family:'Montserrat',sans-serif;color:var(--text);background:var(--white);position:relative}
section,header,footer{position:absolute;left:0;width:1200px}
.abs{position:absolute}
.tick{display:inline-block;width:13px;height:13px;vertical-align:-2px;margin-right:5px}

/* hero */
.hero{top:0;height:662px;background:linear-gradient(160deg,#3a4a5c 0%,#233243 45%,#17212d 100%);color:var(--white)}
.nav-bar{top:0;left:0;width:1200px;height:92px;border-bottom:1px solid rgba(255,255,255,.15)}
.brand{left:63px;top:26px;display:flex;align-items:center;gap:10px;font-weight:600;font-size:30px;letter-spacing:1px;color:var(--white)}
.brand-mark{width:30px;height:30px;background:var(--red)}
.nav{right:65px;top:38px;display:flex;gap:41px;font-size:13px;letter-spacing:.3px}
.nav a{color:var(--white);text-decoration:none}
.nav a.active{color:var(--gold)}
.hero-tag{top:240px;width:1200px;text-align:center;font-family:'Exo 2',sans-serif;font-weight:300;font-size:23px;letter-spacing:.5px}
.hero-address{top:282px;width:1200px;text-align:center;font-weight:700;font-size:37px;line-height:46px}
.hero-address .light{font-family:'Exo 2',sans-serif;font-weight:300;color:var(--gold)}

/* about */
.about{top:662px;height:518px}
.title{font-family:'Exo 2',sans-serif;font-weight:300;font-size:33px;color:var(--text)}
.title b{font-weight:400;color:var(--red)}
.about .title{left:63px;top:76px}
.about-body{left:62px;top:140px;width:585px;font-size:13.4px;line-height:16px;color:var(--text)}
.about-body p{margin-bottom:14px}
.about-body ul{list-style:none;margin:-4px 0 12px}
.about-body li{margin-bottom:9px}
.divider{left:662px;top:136px;width:2px;height:335px;background:#ddd}
.divider i{position:absolute;left:0;top:120px;width:2px;height:120px;background:var(--red)}
.about-photo{left:701px;top:133px;width:435px;height:322px;border-radius:4px;background:linear-gradient(135deg,#b9b3a8,#7c7b77 55%,#4b5360)}

/* experience */
.experience{top:1180px;height:688px;background:var(--navy);color:var(--white)}
.experience .title{width:1200px;text-align:center;top:46px;color:var(--white);font-size:32px}
.exp-intro{top:104px;left:170px;width:860px;text-align:center;font-size:13.4px;line-height:20px}
.exp-card{top:188px;width:344px;height:424px;background:var(--card);border:1px solid var(--card-line);border-radius:3px}
.exp-photo{position:absolute;left:14px;top:14px;width:314px;height:238px;background:linear-gradient(180deg,#d9d9d9,#8a8a8a 60%,#2f2f2f)}
.exp-card h3{position:absolute;left:18px;top:274px;font-family:'Maven Pro',sans-serif;font-weight:500;font-size:23px;color:var(--gold)}
.exp-card p{position:absolute;left:18px;top:316px;width:305px;font-size:13.4px;line-height:16px}
.arrow{width:45px;height:45px;display:flex;align-items:center;justify-content:center}
.exp-arrow{top:375px;background:#5c5447}

/* services */
.services{top:1868px;height:650px}
.srv-photo-a{left:60px;top:65px;width:434px;height:322px;background:linear-gradient(135deg,#2e3f7a,#1d2550 60%,#2a3566)}
.srv-photo-b{left:266px;top:252px;width:272px;height:218px;border:5px solid var(--white);background:linear-gradient(180deg,#c9c9c9,#6c6c6c 50%,#2b2b2b)}
.services .title{left:600px;top:62px;font-size:33px}
.srv-body{left:600px;top:121px;width:525px;font-size:13.4px;line-height:16px}
.srv-body h4{font-size:12.6px;font-weight:600;margin:15px 0 8px}
.srv-body ul{list-style:none}
.srv-body li{margin-bottom:9px}
.srv-line{left:1134px;top:122px;width:2px;height:440px;background:#ddd}
.srv-line i{position:absolute;left:0;top:110px;width:2px;height:120px;background:var(--red)}

/* team */
.team{top:2518px;height:700px;background:var(--team);color:var(--white)}
.team .title{width:1200px;text-align:center;top:50px;color:var(--white);font-size:33px}
.member{top:135px;width:248px;text-align:center}
.member-photo{width:248px;height:288px;background:linear-gradient(180deg,#5a6e86,#3a4658 60%,#1e2532)}
.member h3{margin-top:25px;font-family:'Maven Pro',sans-serif;font-weight:500;font-size:23px;color:var(--gold)}
.member .role{font-family:'Exo 2',sans-serif;font-weight:300;font-size:16px;color:var(--purple);margin-top:2px}
.member p{margin-top:13px;font-size:13.4px;line-height:16px;padding:0 8px}
.dots{top:3154px;left:0;width:1200px;display:flex;justify-content:center;gap:5px}
.dots span{width:10px;height:10px;border-radius:5px;background:#777}
.dots span.on{width:20px;background:var(--red)}

/* contact */
.contact{top:3218px;height:630px;background:var(--light)}
.contact .title{font-size:33px}
.get{left:62px;top:74px}
.form{left:62px;top:140px;width:530px}
.field label{display:block;font-size:13.4px;font-weight:600;margin-bottom:8px}
.field label b{color:var(--red);font-weight:600}
.field .input{height:39px;background:var(--white);border:1px solid #ddd;border-radius:3px;padding:10px 14px;font-size:13px;color:#777}
.row{display:flex;gap:24px}
.row .field{flex:1}
.field{margin-bottom:22px}
.field .area{height:114px}
.submit{left:62px;top:548px;width:109px;height:40px;background:var(--red);border-radius:4px;color:var(--white);font-weight:600;font-size:13.4px;display:flex;align-items:center;justify-content:center}
.contact-head{left:608px;top:74px}
.contact-arrows{left:1039px;top:60px;display:flex;gap:9px}
.contact-arrows .arrow{width:45px;background:#9aa0a8}
.info{left:608px;font-size:17.5px;font-family:'Maven Pro',sans-serif;font-weight:500;line-height:22px;display:flex;gap:12px}
.info svg{flex:none;margin-top:3px}
.map{left:609px;top:286px;width:528px;height:264px;background:linear-gradient(135deg,#dfe6ee,#eef0e8 50%,#cfe0c9)}

.footer{top:3848px;height:56px;background:var(--navy);color:#ddd;font-size:12px;display:flex;align-items:center;justify-content:center}
</style>
</head>
<body>

<header class="hero" role="img" aria-label="Looking up at a dark glass office tower facade">
  <div class="abs nav-bar"></div>
  <div class="abs brand"><span class="brand-mark"></span>TALVERA SERVICES</div>
  <nav class="abs nav">
    <a class="active" href="#">WELCOME</a><a href="#">ABOUT</a><a href="#">EXPERIENCE</a><a href="#">SERVICES</a><a href="#">TEAM</a><a href="#">CONTACT</a>
  </nav>
  <div class="abs hero-tag">YOUR TECHNOLOGY PROJECTS MADE EASY.</div>
  <div class="abs hero-address">LEVEL 2, <span class="light">318 HARLOW STREETMELBOURNE</span><br><span class="light">VIC</span>, 3000, AUSTRALIA 1300 555 018</div>
</header>

<section class="about">
  <h2 class="abs title">About <b>Us</b></h2>
  <div class="abs about-body">
    <p>Talvera Services was established in 2016 by Rob Hartley to provide technology consulting services to corporate and government clients with a focus on:</p>
    <ul>
      <li><svg class="tick" viewBox="0 0 14 14"><circle cx="7" cy="7" r="6" fill="none" stroke="#d7201f" stroke-width="1.3"/><path d="M4 7l2 2 4-4" fill="none" stroke="#d7201f" stroke-width="1.3"/></svg>Property/facilities management</li>
      <li><svg class="tick" viewBox="0 0 14 14"><circle cx="7" cy="7" r="6" fill="none" stroke="#d7201f" stroke-width="1.3"/><path d="M4 7l2 2 4-4" fill="none" stroke="#d7201f" stroke-width="1.3"/></svg>Asset management</li>
      <li><svg class="tick" viewBox="0 0 14 14"><circle cx="7" cy="7" r="6" fill="none" stroke="#d7201f" stroke-width="1.3"/><path d="M4 7l2 2 4-4" fill="none" stroke="#d7201f" stroke-width="1.3"/></svg>Development and Construction</li>
    </ul>
    <p>In 2022, Talvera Services merged Norline Group into its operations, bringing increased capacity and capability to the NSW office.</p>
    <p style="margin-top:26px">Talvera is a privately owned independent consultancy 100% dedicated to customer satisfaction. With experience in a range of technologies such as internet of things, security systems, wifi, building services networks, control centres and smart buildings, our services include</p>
    <ul>
      <li><svg class="tick" viewBox="0 0 14 14"><circle cx="7" cy="7" r="6" fill="none" stroke="#d7201f" stroke-width="1.3"/><path d="M4 7l2 2 4-4" fill="none" stroke="#d7201f" stroke-width="1.3"/></svg>Technology audits</li>
      <li><svg class="tick" viewBox="0 0 14 14"><circle cx="7" cy="7" r="6" fill="none" stroke="#d7201f" stroke-width="1.3"/><path d="M4 7l2 2 4-4" fill="none" stroke="#d7201f" stroke-width="1.3"/></svg>Technology roadmaps</li>
    </ul>
  </div>
  <div class="abs divider"><i></i></div>
  <div class="abs about-photo" role="img" aria-label="Two engineers in hard hats reviewing plans on a laptop, seen from above"></div>
</section>

<section class="experience">
  <h2 class="abs title">EXPERIENCE</h2>
  <p class="abs exp-intro">Talvera has a diverse range of project experience across a range of industries within both the public and private sectors. The following is a small sample of some of the clients and sites we have worked with</p>
  <div class="abs exp-card" style="left:62px">
    <div class="exp-photo" role="img" aria-label="Black and white glass cone roof over a historic tower"></div>
    <h3>Carlton Exchange</h3>
    <p>Security technology design consulting for this popular retail and entertainment hub which is managed by the Harbourline Group</p>
  </div>
  <div class="abs exp-card" style="left:430px">
    <div class="exp-photo" role="img" aria-label="Black and white motorway gantry with passing cars"></div>
    <h3>Southway Link</h3>
    <p>Virtual servers, network and CCTV upgrade design and project management for this landmark road transportation Public Private Partnership (PPP)</p>
  </div>
  <div class="abs exp-card" style="left:795px">
    <div class="exp-photo" role="img" aria-label="Black and white motorway gantry with passing cars"></div>
    <h3>Bayside General Hospital</h3>
    <p>Security technology lifecycle consulting for this leading Health Care Public Private Partnership (PPP) which is operated by Marlow &amp; Finch</p>
  </div>
  <div class="abs arrow exp-arrow" style="left:39px"><svg width="14" height="18" viewBox="0 0 14 18"><path d="M10 2L3 9l7 7" fill="none" stroke="#fff" stroke-width="2"/></svg></div>
  <div class="abs arrow exp-arrow" style="left:1117px"><svg width="14" height="18" viewBox="0 0 14 18"><path d="M4 2l7 7-7 7" fill="none" stroke="#fff" stroke-width="2"/></svg></div>
</section>

<section class="services">
  <div class="abs srv-photo-a" role="img" aria-label="Two technicians working at a server rack"></div>
  <div class="abs srv-photo-b" role="img" aria-label="Black and white close view of network equipment racks"></div>
  <h2 class="abs title">SERVICES</h2>
  <div class="abs srv-body">
    <p>Talvera Services provides independent professional services for projects as well as operations and maintenance. We offer end to end services including</p>
    <h4>Strategy</h4>
    <ul>
      <li><svg class="tick" viewBox="0 0 14 14"><circle cx="7" cy="7" r="6" fill="none" stroke="#d7201f" stroke-width="1.3"/><path d="M4 7l2 2 4-4" fill="none" stroke="#d7201f" stroke-width="1.3"/></svg>Technology roadmaps</li>
      <li><svg class="tick" viewBox="0 0 14 14"><circle cx="7" cy="7" r="6" fill="none" stroke="#d7201f" stroke-width="1.3"/><path d="M4 7l2 2 4-4" fill="none" stroke="#d7201f" stroke-width="1.3"/></svg>Master standards; and</li>
      <li><svg class="tick" viewBox="0 0 14 14"><circle cx="7" cy="7" r="6" fill="none" stroke="#d7201f" stroke-width="1.3"/><path d="M4 7l2 2 4-4" fill="none" stroke="#d7201f" stroke-width="1.3"/></svg>Asset management plans</li>
    </ul>
    <h4>Projects</h4>
    <ul>
      <li><svg class="tick" viewBox="0 0 14 14"><circle cx="7" cy="7" r="6" fill="none" stroke="#d7201f" stroke-width="1.3"/><path d="M4 7l2 2 4-4" fill="none" stroke="#d7201f" stroke-width="1.3"/></svg>Audit</li>
      <li><svg class="tick" viewBox="0 0 14 14"><circle cx="7" cy="7" r="6" fill="none" stroke="#d7201f" stroke-width="1.3"/><path d="M4 7l2 2 4-4" fill="none" stroke="#d7201f" stroke-width="1.3"/></svg>Design</li>
      <li><svg class="tick" viewBox="0 0 14 14"><circle cx="7" cy="7" r="6" fill="none" stroke="#d7201f" stroke-width="1.3"/><path d="M4 7l2 2 4-4" fill="none" stroke="#d7201f" stroke-width="1.3"/></svg>Procurement</li>
      <li><svg class="tick" viewBox="0 0 14 14"><circle cx="7" cy="7" r="6" fill="none" stroke="#d7201f" stroke-width="1.3"/><path d="M4 7l2 2 4-4" fill="none" stroke="#d7201f" stroke-width="1.3"/></svg>Technical project management; and</li>
      <li><svg class="tick" viewBox="0 0 14 14"><circle cx="7" cy="7" r="6" fill="none" stroke="#d7201f" stroke-width="1.3"/><path d="M4 7l2 2 4-4" fill="none" stroke="#d7201f" stroke-width="1.3"/></svg>Witness testing</li>
    </ul>
    <h4>Operations and maintenance</h4>
    <ul>
      <li><svg class="tick" viewBox="0 0 14 14"><circle cx="7" cy="7" r="6" fill="none" stroke="#d7201f" stroke-width="1.3"/><path d="M4 7l2 2 4-4" fill="none" stroke="#d7201f" stroke-width="1.3"/></svg>Service and maintenance specifications</li>
      <li><svg class="tick" viewBox="0 0 14 14"><circle cx="7" cy="7" r="6" fill="none" stroke="#d7201f" stroke-width="1.3"/><path d="M4 7l2 2 4-4" fill="none" stroke="#d7201f" stroke-width="1.3"/></svg>Policies and procedures</li>
      <li><svg class="tick" viewBox="0 0 14 14"><circle cx="7" cy="7" r="6" fill="none" stroke="#d7201f" stroke-width="1.3"/><path d="M4 7l2 2 4-4" fill="none" stroke="#d7201f" stroke-width="1.3"/></svg>Procurement; and</li>
      <li><svg class="tick" viewBox="0 0 14 14"><circle cx="7" cy="7" r="6" fill="none" stroke="#d7201f" stroke-width="1.3"/><path d="M4 7l2 2 4-4" fill="none" stroke="#d7201f" stroke-width="1.3"/></svg>Service reviews</li>
    </ul>
  </div>
  <div class="abs srv-line"><i></i></div>
</section>

<section class="team">
  <h2 class="abs title">OUR <b>TEAM</b></h2>
  <div class="abs member" style="left:64px">
    <div class="member-photo" role="img" aria-label="Portrait of team member"></div>
    <h3>Rob Hartley</h3><div class="role">Principal Consultant</div>
    <p>Rob founded Talvera in 2016 and continues to lead the organisation nationally</p>
  </div>
  <div class="abs member" style="left:339px">
    <div class="member-photo" role="img" aria-label="Portrait of team member"></div>
    <h3>Grant Ellison</h3><div class="role">Principal Consultant</div>
    <p>Grant founded Norline Group in 2016 and joined Talvera as a Director in 2022, taking over leadership of the NSW office</p>
  </div>
  <div class="abs member" style="left:611px">
    <div class="member-photo" role="img" aria-label="Portrait of team member"></div>
    <h3>Daniel Corrigan</h3><div class="role">Senior Consultant</div>
    <p>Daniel joined Talvera in 2016 and continues to lead the organisation nationally</p>
  </div>
  <div class="abs member" style="left:889px">
    <div class="member-photo" role="img" aria-label="Portrait of team member"></div>
    <h3>Mark Tessler</h3><div class="role">Senior Consultant</div>
    <p>Mark joined Talvera in 2020 to help grow the business both in Melbourne and nationally. In 2021, Mark relocated to Sydney to establish Talvera's New South Wales office</p>
  </div>
</section>
<div class="abs dots"><span class="on"></span><span></span><span></span></div>

<section class="contact">
  <h2 class="abs title get">Get in <b>Touch</b></h2>
  <div class="abs form">
    <div class="row">
      <div class="field"><label>First Name<b>*</b></label><div class="input">First Name</div></div>
      <div class="field"><label>Last Name<b>*</b></label><div class="input">Last Name</div></div>
    </div>
    <div class="field"><label>Email Address<b>*</b></label><div class="input">Email Address</div></div>
    <div class="field"><label>Subject<b>*</b></label><div class="input">Subject</div></div>
    <div class="field"><label>Message<b>*</b></label><div class="input area">Message</div></div>
  </div>
  <div class="abs submit">SUBMIT</div>

  <h2 class="abs title contact-head">Contact</h2>
  <div class="abs contact-arrows">
    <div class="arrow"><svg width="14" height="18" viewBox="0 0 14 18"><path d="M10 2L3 9l7 7" fill="none" stroke="#fff" stroke-width="2"/></svg></div>
    <div class="arrow"><svg width="14" height="18" viewBox="0 0 14 18"><path d="M4 2l7 7-7 7" fill="none" stroke="#fff" stroke-width="2"/></svg></div>
  </div>
  <div class="abs info" style="top:140px"><svg width="16" height="20" viewBox="0 0 16 20"><path d="M8 1a6 6 0 0 1 6 6c0 5-6 12-6 12S2 12 2 7a6 6 0 0 1 6-6z" fill="none" stroke="#d7201f" stroke-width="1.5"/><circle cx="8" cy="7" r="2" fill="none" stroke="#d7201f" stroke-width="1.5"/></svg><span>GPO Box 4120<br>MELBOURNE VIC 3001</span></div>
  <div class="abs info" style="top:196px"><svg width="18" height="18" viewBox="0 0 18 18"><path d="M4 2l3 3-2 2c1 2 3 4 5 5l2-2 3 3-2 3C7 15 3 11 2 5z" fill="none" stroke="#d7201f" stroke-width="1.5"/></svg><span>1300 555 018</span></div>
  <div class="abs info" style="top:230px"><svg width="18" height="14" viewBox="0 0 18 14"><rect x="1" y="1" width="16" height="12" fill="none" stroke="#d7201f" stroke-width="1.5"/><path d="M1 1l8 6 8-6" fill="none" stroke="#d7201f" stroke-width="1.5"/></svg><span>hello@talvera.com.au</span></div>
  <div class="abs map" role="img" aria-label="Street map of central Melbourne with office location"></div>
</section>

<footer class="footer">Talvera Services Pty Ltd &nbsp;|&nbsp; ABN: 12 345 678 901</footer>

</body>
</html>
```